Deactivated Coal-Fired Power Plant to be redeveloped into a Green Energy Campus.

Want a striking business card statement that introduces our concept project to provide economic and community recovery to a former rural coal community in western PA.
Essentially 12 project representatives that will lead both the demolition of an existing power plant and the redevelopment to a new Green energy site.
Business Card should reflect our effort.
We are open to ideas.

Target Market(s)

Energy and Power Generation industries

Industry/Entity Type

Power Generation and Data Centers

Contact Information for Business Card

Included in uploaded materials

Font styles to use
Sans Serif
Other font styles liked:
• Arial, Calibri

Requirements
Must have
• Multiple colors

```html
<!DOCTYPE html>
<html lang="en">
<head>
<meta charset="utf-8">
<title>Ridgeline Renewal – Business Card</title>
<link rel="stylesheet" href="https://fonts.googleapis.com/css2?family=Open+Sans:wght@300;400;600;700&display=swap">
<style>
  :root {
    --backdrop: #717171;
    --brand-green: #13974a;
    --deep-green: #0d6e34;
    --card-white: #ececec;
    --ink: #1a1a1a;
    --rule: #7a7a7a;
    --ghost: #dedede;
  }
  * { margin: 0; padding: 0; box-sizing: border-box; }
  html, body { width: 1200px; height: 1000px; overflow: hidden; }
  body {
    background: var(--backdrop);
    font-family: "Open Sans", Arial, sans-serif;
    position: relative;
  }
  .card {
    position: absolute;
    width: 614px;
    height: 351px;
  }
  .card--front {
    left: 291px; top: 143px;
    background: var(--brand-green);
    display: flex; align-items: center; justify-content: center;
  }
  .front-wordmark {
    display: flex; align-items: center; gap: 14px;
    color: var(--deep-green);
    font-weight: 700;
    font-size: 30px;
    letter-spacing: 1px;
    margin-top: 30px;
  }
  .front-wordmark .mark-dot {
    width: 26px; height: 26px; border-radius: 50%;
    background: var(--deep-green);
  }
  .card--back {
    left: 294px; top: 542px;
    background: var(--card-white);
    overflow: hidden;
  }
  .back-wordmark {
    position: absolute; left: 32px; top: 44px;
    display: flex; align-items: center; gap: 10px;
    color: var(--ink);
    font-weight: 700;
    font-size: 20px;
  }
  .back-wordmark .mark-dot {
    width: 22px; height: 22px; border-radius: 50%;
    background: var(--brand-green);
  }
  .ghost-wordmark {
    position: absolute; left: 300px; top: 140px;
    width: 300px;
    color: var(--ghost);
    font-weight: 700;
    font-size: 44px;
    line-height: 1.05;
    text-align: center;
  }
  .person-name {
    position: absolute; left: 36px; top: 208px;
    color: var(--brand-green);
    font-weight: 600;
    font-size: 21px;
    letter-spacing: 1.5px;
  }
  .person-title {
    position: absolute; left: 36px; top: 240px;
    color: var(--ink);
    font-size: 10px;
    letter-spacing: 2.4px;
  }
  .contact-rule {
    position: absolute; left: 36px; top: 263px;
    width: 541px; height: 2px;
    background: var(--rule);
  }
  .contact-email {
    position: absolute; left: 36px; top: 272px;
    color: var(--ink);
    font-weight: 300;
    font-size: 16px;
  }
  .contact-phone {
    position: absolute; left: 36px; top: 293px;
    color: var(--brand-green);
    font-weight: 600;
    font-size: 16px;
  }
</style>
</head>
<body>
  <section class="card card--front">
    <div class="front-wordmark"><span class="mark-dot"></span>RIDGELINE RENEWAL</div>
  </section>

  <section class="card card--back">
    <div class="back-wordmark"><span class="mark-dot"></span>RIDGELINE RENEWAL</div>
    <div class="ghost-wordmark" aria-hidden="true">RIDGELINE RENEWAL</div>
    <div class="person-name">DANIEL&nbsp; ARCAND</div>
    <div class="person-title">CHIEF OPERATING OFFICER</div>
    <div class="contact-rule"></div>
    <div class="contact-email">darcand@ridgelinerenewal.com</div>
    <div class="contact-phone">(555) 014 2870</div>
  </section>
</body>
</html>
```